Zabrin Design Prize - $10,000 tablet app design contest, Brochure Category

Zabrin is a marketplace for iSlate App Templates (similar to PageForge templates). We want you to design an app template for sale in our marketplace which targets Brochure Apps (iSlate Apps for examples like travel brochure, university prospectus, music guide for a venue).

It’s up to you to create pages or features for the App Template that you think are appropriate. Creativity will be rewarded! Here are some example pages or features that you could create:

• Welcome page
• Guides to places, events etc.
• Maps - countries, local venue guide, university campuses etc.
• Contact page
• Hyperlinks to webpages
• Social media integration
• Animations and video

Your design should be Vibrant, Engaging and Contemporary. If you have an iSlate, download Zabrin Viewer and download template examples in the download tab.

Your entry must include:
• A brief description of your template
• Preview images of all pages of your template

Attached to this project are free templates to help you get started with your design. We have included:
1. A free portfolio template for designers/photographers
2. Icons and artwork to use in your template
3. Blank pages template
4. Form template
5. Video ad template

If you are selected as a finalist you will be required to submit an .zproject file containing:
• Your LayoutPro source files
• Preview images of your template
• All creative / stock assets used in the template (animations, video etc.)
• A text file with instructions on how to update the template
• A metadata .txt file containing template details and your information

How to enter:
1. Register at Marketplace and view the instructions under the welcome message https://marketplace.zabrinhub.example/welcome
2. Download Zabrin Editor: https://support.zabrinhub.example/entries/48150926-zabrin-editor
3. Use the free templates provided in this brief to create your designs and submit to PlanGather
Updates

Project Deadline Extended
Reason: Due to the Christmas break we are extending the deadline of our competition. Thank you for time and effort - I will be providing feedback over the next couple of days! Best wishes, Melika

Hi All,

I have received many screenshots with some great designs! I just wanted to clarify that you are designing Zabrin app templates including Zabrin features and not just page designs?

Read Tips for First Time Zabriners to guide you through the template creation process

Before you start designing templates for Zabrin Marketplace

·       Read the Quality Standards

·       Read the Copyright Information 

·       Use the Template Quality Checklist to ensure your template follows our guidelines. 

What should my project file contain?

·       A folder containing your source files, e.g. LayoutPro. This must be named Source.

·       The Zabrin content files. This must be named Bundle.

·       Instructions, explaining to a customer how to use your template.

Best wishes,

Melika

Project Deadline Extended
Reason: We are extending the competition by 7 days to give you more time!

Project Deadline Extended
Reason: We have received 3 complete designs for this contest so we are extending the deadline by 7 days. Melika :)

Target Market(s)

Entrepreneurs who wish to create iSlate Apps by using our App design templates.

Industry/Entity Type

University

Requirements
Must have
• You will need Zabrin Editor to open the .zproject files attached to this brief. Get it here: https://support.zabrinhub.example/entries/48150926-zabrin-editor
Should not have
• • Low quality, fuzzy or blurry images
• Any stock images or content which you do not own the rights to
• Any material which could be considered inappropriate or offensive

```html
<!DOCTYPE html>
<html lang="en">
<head>
<meta charset="utf-8">
<title>Zabrin Brochure Template – Get Out There</title>
<link rel="stylesheet" href="https://fonts.googleapis.com/css2?family=Montserrat:wght@500;600&family=Questrial&display=swap">
<style>
  :root {
    --canvas: #ffffff;
    --white: #ffffff;
    --panel-dark: rgba(40, 40, 40, 0.82);
    --nature-1: #a8e020; --nature-2: #5fcf1a; --nature-3: #c8ea2a;
    --culture-1: #c21ed8; --culture-2: #8a2be2; --culture-3: #e045f0;
    --cold-1: #1a8fe0; --cold-2: #14c8d8; --cold-3: #36a8f0;
    --warm-1: #f0b400; --warm-2: #e8641a; --warm-3: #f5d020;
  }
  * { box-sizing: border-box; margin: 0; padding: 0; }
  html, body { width: 1200px; height: 904px; overflow: hidden; background: var(--canvas); }
  body { position: relative; font-family: "Montserrat", sans-serif; }

  .page {
    position: absolute; width: 589px; height: 441px; overflow: hidden;
    box-shadow: 0 2px 6px rgba(0,0,0,0.45);
  }
  .page--nature  { left: 0;     top: 0; }
  .page--culture { left: 611px; top: 0; }
  .page--cold    { left: 0;     top: 463px; }
  .page--warm    { left: 611px; top: 463px; }

  .page__photo { position: absolute; inset: 0; }
  .page--nature .page__photo  { background: linear-gradient(180deg, #5c6470 0%, #8a8e88 24%, #6e7a3a 36%, #c9b48a 55%, #d8c6a2 100%); }
  .page--culture .page__photo { background: linear-gradient(180deg, #b8cce0 0%, #c9d6e2 30%, #b89a7c 45%, #8a9a86 62%, #7f9e90 100%); }
  .page--cold .page__photo    { background: linear-gradient(180deg, #4a7fc8 0%, #9cc0e6 22%, #5a7060 38%, #e8eef6 58%, #f8fbff 100%); }
  .page--warm .page__photo    { background: linear-gradient(180deg, #2c57a8 0%, #5a86c8 30%, #a89070 52%, #b89a80 72%, #8a7058 100%); }

  .mosaic { position: absolute; }
  .mosaic rect { opacity: 0.88; }

  .page__title {
    position: absolute; top: 14px; left: 22px;
    font-family: "Questrial", "Montserrat", sans-serif;
    font-size: 62px; line-height: 1; color: var(--white);
    letter-spacing: 0.28em; white-space: nowrap;
    text-shadow: 0 1px 3px rgba(0,0,0,0.25);
  }
  .page--cold .page__title, .page--warm .page__title { letter-spacing: 0.42em; top: 18px; }

  .gallery-icon { position: absolute; left: 9px; bottom: 10px; width: 49px; height: 49px; }

  .page-number {
    position: absolute; right: 18px; bottom: 16px;
    font-family: "Montserrat", sans-serif; font-weight: 600; font-size: 24px; color: var(--white);
  }

  .toolbar {
    position: absolute; left: 358px; right: 0; top: 390px; height: 30px;
    background: linear-gradient(90deg, var(--panel-dark) 60%, rgba(40,40,40,0));
    display: flex; gap: 4px; padding: 2px 0 0 2px;
  }
  .page--culture .toolbar { left: 359px; top: 389px; }
  .toolbar__btn { width: 26px; height: 26px; }

  .info-card {
    position: absolute; left: 358px; top: 153px; width: 209px; height: 229px;
    background: var(--panel-dark); color: var(--white); padding: 8px 10px;
  }
  .info-card__heading {
    font-family: "Questrial", sans-serif; font-size: 22px; letter-spacing: 0.2em; line-height: 1.1;
    margin-bottom: 3px;
  }
  .info-card__body {
    font-family: "Questrial", sans-serif; font-size: 10px; line-height: 1.25; text-align: justify;
  }
  .info-card__body + .info-card__body { margin-top: 10px; }

  .location-card__map {
    display: block; width: 189px; height: 185px; margin-top: 4px;
    background: linear-gradient(160deg, #cfe3a8 0%, #e8efc8 35%, #b6d2e8 60%, #a8c8e4 100%);
  }
</style>
</head>
<body>

<svg width="0" height="0" style="position:absolute">
  <defs>
    <symbol id="icon-gallery" viewBox="0 0 49 49">
      <rect x="0.5" y="0.5" width="48" height="48" rx="4" fill="#fff"/>
      <rect x="7" y="7" width="26" height="26" fill="none" stroke="#444" stroke-width="2"/>
      <rect x="11" y="11" width="26" height="26" fill="none" stroke="#444" stroke-width="2"/>
      <rect x="15" y="15" width="27" height="27" fill="#fff" stroke="#444" stroke-width="2.5"/>
    </symbol>
    <symbol id="icon-info" viewBox="0 0 26 26">
      <rect width="26" height="26" rx="2" fill="#fff"/>
      <circle cx="13" cy="6" r="2.6" fill="#333"/>
      <rect x="10.5" y="10" width="5" height="12" fill="#333"/>
    </symbol>
    <symbol id="icon-pin" viewBox="0 0 26 26">
      <rect width="26" height="26" rx="2" fill="#fff"/>
      <path d="M13 3a6.5 6.5 0 0 0-6.5 6.5c0 4.6 6.5 13.5 6.5 13.5s6.5-8.9 6.5-13.5A6.5 6.5 0 0 0 13 3z" fill="#333"/>
      <circle cx="13" cy="9.5" r="2.4" fill="#fff"/>
    </symbol>
  </defs>
</svg>

<!-- Nature -->
<section class="page page--nature">
  <div class="page__photo" role="img" aria-label="Photo: sand dunes with footprints leading towards green hills under a cloudy sky"></div>
  <svg class="mosaic" style="left:14px;top:12px" width="200" height="110" aria-hidden="true">
    <rect x="0" y="40" width="30" height="30" fill="var(--nature-2)"/><rect x="22" y="20" width="28" height="28" fill="var(--nature-1)"/>
    <rect x="50" y="10" width="34" height="34" fill="var(--nature-2)"/><rect x="80" y="30" width="30" height="30" fill="var(--nature-3)"/>
    <rect x="110" y="18" width="32" height="32" fill="var(--nature-1)"/><rect x="140" y="40" width="30" height="30" fill="var(--nature-2)"/>
    <rect x="170" y="20" width="24" height="24" fill="var(--nature-3)"/><rect x="30" y="60" width="28" height="28" fill="var(--nature-3)"/>
    <rect x="10" y="80" width="24" height="24" fill="var(--nature-2)"/><rect x="120" y="58" width="26" height="26" fill="var(--nature-1)"/>
  </svg>
  <h2 class="page__title">GET NATURE</h2>
  <svg class="mosaic" style="right:8px;bottom:10px" width="110" height="68" aria-hidden="true">
    <rect x="80" y="0" width="20" height="20" fill="var(--nature-2)"/><rect x="60" y="20" width="22" height="22" fill="var(--nature-1)"/>
    <rect x="30" y="36" width="24" height="16" fill="var(--nature-3)"/><rect x="0" y="44" width="30" height="12" fill="var(--nature-2)"/>
    <rect x="50" y="48" width="26" height="18" fill="var(--nature-2)"/><rect x="84" y="26" width="20" height="30" fill="var(--nature-1)"/>
  </svg>
  <svg class="gallery-icon" aria-label="Gallery"><use href="#icon-gallery"/></svg>
  <span class="page-number">1</span>
</section>

<!-- Culture -->
<section class="page page--culture">
  <div class="page__photo" role="img" aria-label="Photo: canal lined with historic buildings, boats on green water"></div>
  <svg class="mosaic" style="left:20px;top:10px" width="200" height="160" aria-hidden="true">
    <rect x="0" y="30" width="30" height="30" fill="var(--culture-1)"/><rect x="30" y="10" width="30" height="30" fill="var(--culture-3)"/>
    <rect x="62" y="28" width="34" height="34" fill="var(--culture-2)"/><rect x="96" y="8" width="28" height="28" fill="var(--culture-1)"/>
    <rect x="130" y="34" width="34" height="34" fill="var(--culture-3)"/><rect x="40" y="60" width="26" height="26" fill="var(--culture-1)"/>
    <rect x="48" y="108" width="30" height="30" fill="var(--culture-3)"/><rect x="90" y="100" width="22" height="22" fill="var(--culture-2)"/>
    <rect x="80" y="130" width="30" height="26" fill="var(--culture-1)"/><rect x="120" y="140" width="40" height="16" fill="var(--culture-3)"/>
  </svg>
  <h2 class="page__title">GET CULTURE</h2>
  <div class="toolbar">
    <svg class="toolbar__btn" aria-label="Information"><use href="#icon-info"/></svg>
    <svg class="toolbar__btn" aria-label="Location"><use href="#icon-pin"/></svg>
  </div>
  <svg class="mosaic" style="right:6px;bottom:12px" width="110" height="68" aria-hidden="true">
    <rect x="88" y="0" width="18" height="20" fill="var(--culture-1)"/><rect x="70" y="18" width="24" height="24" fill="var(--culture-3)"/>
    <rect x="30" y="40" width="30" height="14" fill="var(--culture-2)"/><rect x="0" y="42" width="30" height="10" fill="var(--culture-1)"/>
    <rect x="58" y="44" width="28" height="20" fill="var(--culture-1)"/><rect x="90" y="26" width="18" height="30" fill="var(--culture-2)"/>
  </svg>
  <svg class="gallery-icon" aria-label="Gallery"><use href="#icon-gallery"/></svg>
  <span class="page-number">1</span>
</section>

<!-- Cold -->
<section class="page page--cold">
  <div class="page__photo" role="img" aria-label="Photo: snow-covered fir trees on a snowy slope beneath a blue sky"></div>
  <svg class="mosaic" style="left:275px;top:10px" width="250" height="130" aria-hidden="true">
    <rect x="0" y="18" width="40" height="40" fill="var(--cold-3)"/><rect x="40" y="0" width="40" height="40" fill="var(--cold-1)"/>
    <rect x="70" y="40" width="46" height="46" fill="var(--cold-2)"/><rect x="110" y="10" width="40" height="40" fill="var(--cold-3)"/>
    <rect x="150" y="30" width="40" height="40" fill="var(--cold-1)"/><rect x="180" y="60" width="44" height="44" fill="var(--cold-2)"/>
    <rect x="8" y="64" width="38" height="38" fill="var(--cold-1)"/><rect x="120" y="70" width="36" height="36" fill="var(--cold-3)"/>
    <rect x="210" y="14" width="30" height="30" fill="var(--cold-3)"/><rect x="200" y="100" width="30" height="24" fill="var(--cold-1)"/>
  </svg>
  <h2 class="page__title">GET COLD</h2>
  <article class="info-card">
    <h3 class="info-card__heading">Information</h3>
    <p class="info-card__body">Tas molupta tectoreptat audis quassi ut res cus eatibus apitae la similique volorpotate consend aecerit et in repedis exeriam, quis essumquuntis dunt et plabor sectus est quiandandis autem hario. Volorepera seque eosto veritas estrunti coresed maximposam fugiandam que vendit quibus samust eturi audi ullorro que veritae ritiur aut andi quo doluptatque con non nis re a vitiam, arciliq uatenem as exerchil et qui blaccatin pore, omnis platur?</p>
    <p class="info-card__body">Arum alici in porit, sed quam excea volorro et quid endant ex et oditium.</p>
  </article>
  <div class="toolbar">
    <svg class="toolbar__btn" aria-label="Information"><use href="#icon-info"/></svg>
    <svg class="toolbar__btn" aria-label="Location"><use href="#icon-pin"/></svg>
  </div>
  <svg class="mosaic" style="right:6px;bottom:10px" width="110" height="68" aria-hidden="true">
    <rect x="88" y="0" width="18" height="20" fill="var(--cold-1)"/><rect x="70" y="18" width="24" height="24" fill="var(--cold-2)"/>
    <rect x="30" y="40" width="30" height="16" fill="var(--cold-3)"/><rect x="0" y="44" width="30" height="12" fill="var(--cold-1)"/>
    <rect x="58" y="44" width="28" height="22" fill="var(--cold-2)"/><rect x="90" y="26" width="18" height="30" fill="var(--cold-3)"/>
  </svg>
  <svg class="gallery-icon" aria-label="Gallery"><use href="#icon-gallery"/></svg>
  <span class="page-number">1</span>
</section>

<!-- Warm -->
<section class="page page--warm">
  <div class="page__photo" role="img" aria-label="Photo: tall cactus in a dry rocky desert valley under a blue sky"></div>
  <svg class="mosaic" style="left:325px;top:10px" width="250" height="140" aria-hidden="true">
    <rect x="60" y="0" width="38" height="38" fill="var(--warm-3)"/><rect x="100" y="14" width="40" height="40" fill="var(--warm-1)"/>
    <rect x="20" y="40" width="34" height="34" fill="var(--warm-1)"/><rect x="60" y="44" width="42" height="42" fill="var(--warm-2)"/>
    <rect x="140" y="30" width="40" height="40" fill="var(--warm-2)"/><rect x="180" y="60" width="44" height="44" fill="var(--warm-2)"/>
    <rect x="0" y="70" width="40" height="40" fill="var(--warm-3)"/><rect x="120" y="72" width="34" height="34" fill="var(--warm-1)"/>
    <rect x="200" y="20" width="34" height="34" fill="var(--warm-3)"/><rect x="190" y="104" width="30" height="26" fill="var(--warm-1)"/>
  </svg>
  <h2 class="page__title">GET WARM</h2>
  <article class="info-card location-card">
    <h3 class="info-card__heading">Location</h3>
    <div class="location-card__map" role="img" aria-label="Map of southern South America with a location marker"></div>
  </article>
  <div class="toolbar">
    <svg class="toolbar__btn" aria-label="Information"><use href="#icon-info"/></svg>
    <svg class="toolbar__btn" aria-label="Location"><use href="#icon-pin"/></svg>
  </div>
  <svg class="mosaic" style="right:6px;bottom:10px" width="110" height="68" aria-hidden="true">
    <rect x="88" y="0" width="18" height="20" fill="var(--warm-1)"/><rect x="70" y="18" width="24" height="24" fill="var(--warm-3)"/>
    <rect x="30" y="40" width="30" height="16" fill="var(--warm-2)"/><rect x="0" y="44" width="30" height="12" fill="var(--warm-1)"/>
    <rect x="58" y="44" width="28" height="22" fill="var(--warm-2)"/><rect x="90" y="26" width="18" height="30" fill="var(--warm-1)"/>
  </svg>
  <svg class="gallery-icon" aria-label="Gallery"><use href="#icon-gallery"/></svg>
  <span class="page-number">2</span>
</section>

</body>
</html>
```